Reaching the Root: Reasoning in Clinical Choice-Making

I'd like a cover that looks like it would fit on the shelf next to "The Symptom Mirage" by Harold Vintner, "The Fall of Forgetting" by Carl Mortenson, "Meal Mend" by Neil Forsby, "The Energy Renewal Plan" by Owen Prichardson or "The Gland Renewal Plan" by the same or "The Cortex Renewal Plan" by the same ... either text only (with some interesting fonts that make the title stand out, and the subtitle smaller) or a relevant image, though I'm not entirely sure what that would be since this is a book about big-picture medical decision making.
Author name is Dr Miriam Oakhurst, NMD
I'll eventually request an e-book, paperback, and audio cover from the winner...

Target Market(s)

practicing physicians

Industry/Entity Type

medicine

Requirements
Must have
• look similar to other books in the genre

```html
<!DOCTYPE html>
<html lang="en">
<head>
<meta charset="utf-8">
<title>Reaching the Root: Reasoning in Clinical Choice-Making — Book Cover</title>
<link rel="stylesheet" href="https://fonts.googleapis.com/css2?family=Anton&family=Open+Sans:ital,wght@0,400;1,800&family=Tinos:wght@700&display=swap">
<style>
  :root {
    --page-bg: #ffffff;
    --cover-blue: #12b0d8;
    --ink: #000000;
    --paper: #ffffff;
  }
  html, body {
    margin: 0;
    padding: 0;
    width: 1200px;
    height: 1200px;
    overflow: hidden;
    background: var(--page-bg);
  }
  .cover {
    display: block;
    width: 1200px;
    height: 1200px;
  }
  .cover-panel { fill: var(--cover-blue); }
  .bestseller-flag {
    font-family: "Open Sans", sans-serif;
    font-style: italic;
    font-weight: 800;
    font-size: 39px;
    fill: var(--paper);
  }
  .title-lead {
    font-family: "Open Sans", sans-serif;
    font-weight: 400;
    font-size: 45px;
    fill: var(--ink);
  }
  .title-main {
    font-family: "Anton", "Impact", sans-serif;
    fill: var(--ink);
  }
  .title-joiner {
    font-family: "Open Sans", sans-serif;
    font-weight: 400;
    font-size: 54px;
    fill: var(--ink);
  }
  .tagline {
    font-family: "Open Sans", sans-serif;
    font-weight: 400;
    font-size: 33px;
    fill: var(--ink);
  }
  .author-name {
    font-family: "Tinos", "Times New Roman", serif;
    font-weight: 700;
    font-size: 56px;
    fill: var(--ink);
  }
</style>
</head>
<body>
<svg class="cover" viewBox="0 0 1200 1200" xmlns="http://www.w3.org/2000/svg" role="img" aria-label="Book cover: Reaching the Root: Reasoning in Clinical Choice-Making by Dr Miriam Oakhurst, NMD">
  <rect class="cover-panel" x="222" y="34" width="762" height="1137"/>

  <text class="bestseller-flag" x="604" y="120" text-anchor="middle">METRO LEDGER BESTSELLER</text>

  <text class="title-lead" x="604" y="234" text-anchor="middle">Reaching the Root:</text>

  <g class="title-block">
    <text class="title-main" x="361" y="411" font-size="186" textLength="452" lengthAdjust="spacingAndGlyphs">REASONING</text>
    <text class="title-joiner" x="818" y="411">in</text>
    <text class="title-main" x="360" y="530" font-size="123" textLength="454" lengthAdjust="spacingAndGlyphs">CLINICAL</text>
    <text class="title-main" x="362" y="630" font-size="106" textLength="450" lengthAdjust="spacingAndGlyphs">CHOICE-</text>
    <text class="title-main" x="354" y="762" font-size="140" textLength="466" lengthAdjust="spacingAndGlyphs">MAKING</text>
  </g>

  <g class="tagline-block">
    <text class="tagline" x="394" y="834">Lorem ipsum dolor sit amet,</text>
    <text class="tagline" x="394" y="878">consectetuer adipiscing elit,</text>
  </g>

  <text class="author-name" x="604" y="1062" text-anchor="middle">Dr Miriam Oakhurst, NMD</text>
</svg>
</body>
</html>
```